Plum Stride Buisiness card

needing a Business card for our company - Plum Stride.
Plum stride is co owned by Nell and Dermot Wardrop (Husband and Wife)
Services Plum Stride provides include:
Dietetic/nutrition Consultations, weight loss coaching programs, personal and group training, post injury rehab, health and nutrition presentations and Health Retreats.
Nell:
Accredited Practicing Dietitian & Personal trainer
Dermot:
Personal trainer, rehab trainer & Strength and conditioning coach
At this stage the business cards will be made just for Nell.
She has a training studio in Armadale and Dietetics private practice in Richmond.
Mobile services are also available (i.e. meet at house or local cafe)

We need the card to look smart, modern and combine both nutrition and training.
We already have a logo which I will attach.
I was initial thinking i black background but am open to suggestions.

Target Market(s)

Health concious, People with money,

Industry/Entity Type

Nutrition

Contact Information for Business Card

Plum Stride
Nell Wardrop
M: 0431907265
E: plumstride@postwren.com
W: www.plumstride.com.au
Address:
Dietetics: Level 1, 88 Tolley Street
Richmond VIC 3121
Training: Private Studio, behind 517 Merrow St
ARMADALE, VIC, 3143

Requirements
Must have
• Must have logo (see attached) please not the one we use is the top left (blue and green)
please note attachment is top left (green and blue)

needs to be clear to read - the font needs to be clear and sharp and the background cannot be too busy.eg funny patterns.
Could I please see a card with a line for 'appointment time/date:' possibly on the back. Would like to see what this looks like.
Nell Wardrop's Profile (side of card) must include "Accredited Practicing Dietitian" and "Personal Trainer."
I like when the services plum stride provide are in dot form.
Nice to have
• would like the card to be 2 sides
first side:
Plum stride logo - Large
services plum stride provides: Dietetic/nutrition Consultations, weight loss coaching programs, personal and group training, post injury rehab, health and nutrition presentations and Health Retreats.
web address
second side:
smaller logo
Details for Nell:
Accredited Practicing Dietitian
Personal Trainer
Contact Details:
M: 0431907265
E: plumstride@postwren.com
Address:
Richmond VIC 3121
ARMADALE, VIC, 3143
Should not have
• Dietetic + nutrition consultations
Should say dietetic/nutrition consultations (first letter of words in capitals please)
Please write phone number as 0431 907 265
Not: 04 31 907265
- note numbers as 4, 3, 3.

```html
<!DOCTYPE html>
<html lang="en">
<head>
<meta charset="utf-8">
<title>Plum Stride – Business Card</title>
<link href="https://fonts.googleapis.com/css2?family=Open+Sans:ital,wght@0,400;0,600;0,700;1,400&family=Roboto+Condensed:wght@700&display=swap" rel="stylesheet">
<style>
  :root {
    --stage: #2b2b2b;
    --card: #ffffff;
    --brand-blue: #1f6fb8;
    --deep-blue: #0b4ea2;
    --plum: #7b3294;
    --grey-text: #555a60;
  }
  * { margin: 0; padding: 0; box-sizing: border-box; }
  html, body {
    width: 1200px; height: 900px; overflow: hidden;
    background: var(--stage);
    font-family: "Open Sans", Arial, sans-serif;
  }
  .stage { position: relative; width: 1200px; height: 900px; }
  .card {
    position: absolute; left: 290px; width: 620px; height: 354px;
    background: var(--card); overflow: hidden;
    box-shadow: 0 10px 30px rgba(0,0,0,.45);
  }
  .card--profile { top: 62px; }
  .card--services { top: 476px; }

  .card__bands { position: absolute; left: 0; bottom: 0; width: 620px; height: 40px; }

  /* brand lockup: plain circle + name */
  .brand { position: absolute; display: flex; align-items: center; gap: 10px; }
  .brand__dot { flex: none; border-radius: 50%; border: 3px solid var(--brand-blue); }
  .brand__name { color: var(--brand-blue); font-weight: 400; line-height: 1; letter-spacing: -0.5px; white-space: nowrap; }

  .card--profile .brand { top: 28px; right: 34px; }
  .card--profile .brand__dot { width: 34px; height: 34px; }
  .card--profile .brand__name { font-size: 26px; }

  .card--services .brand { top: 56px; left: 178px; }
  .card--services .brand__dot { width: 62px; height: 62px; }
  .card--services .brand__name { font-size: 48px; }

  /* profile side */
  .profile { position: absolute; left: 42px; top: 128px; }
  .profile__role { font-family: "Roboto Condensed", "Arial Narrow", sans-serif; font-weight: 700; font-size: 22px; line-height: 1.2; }
  .profile__role--dietitian { color: var(--deep-blue); }
  .profile__role--trainer { color: var(--plum); margin-left: 14px; }
  .contact { list-style: none; margin-top: 12px; margin-left: 14px; }
  .contact__item { display: flex; align-items: center; gap: 12px; font-size: 12.5px; color: var(--grey-text); line-height: 22px; white-space: nowrap; }
  .contact__icon { width: 14px; height: 14px; flex: none; fill: none; stroke: var(--deep-blue); stroke-width: 1.6; }

  /* services side */
  .services { position: absolute; left: 42px; top: 176px; list-style: none; }
  .services__item { position: relative; padding-left: 22px; color: var(--plum); font-style: italic; font-size: 17px; line-height: 25px; white-space: nowrap; }
  .services__item::before { content: ""; position: absolute; left: 2px; top: 11px; width: 6px; height: 6px; border-radius: 50%; background: var(--deep-blue); }
  .web { position: absolute; left: 42px; top: 270px; color: var(--deep-blue); font-weight: 700; font-size: 17px; letter-spacing: 0.3px; }
</style>
</head>
<body>
<main class="stage">

  <section class="card card--profile" aria-label="Profile side">
    <div class="brand">
      <span class="brand__dot" aria-hidden="true"></span>
      <span class="brand__name">Plum Stride</span>
    </div>

    <div class="profile">
      <p class="profile__role profile__role--dietitian">Accredited Practicing Dietitian</p>
      <p class="profile__role profile__role--trainer">Personal Trainer</p>
      <ul class="contact">
        <li class="contact__item">
          <svg class="contact__icon" viewBox="0 0 14 14" aria-hidden="true"><rect x="3.5" y="1" width="7" height="12" rx="1.2"/><line x1="6" y1="11" x2="8" y2="11"/></svg>
          0431907265
        </li>
        <li class="contact__item">
          <svg class="contact__icon" viewBox="0 0 14 14" aria-hidden="true"><rect x="1" y="3" width="12" height="8.5" rx="1"/><polyline points="1.5,3.5 7,8 12.5,3.5"/></svg>
          plumstride@postwren.com
        </li>
        <li class="contact__item">
          <svg class="contact__icon" viewBox="0 0 14 14" aria-hidden="true"><circle cx="7" cy="7" r="5.8"/><ellipse cx="7" cy="7" rx="2.6" ry="5.8"/><line x1="1.2" y1="7" x2="12.8" y2="7"/></svg>
          www.plumstride.com.au
        </li>
        <li class="contact__item">
          <svg class="contact__icon" viewBox="0 0 14 14" aria-hidden="true"><path d="M7 13s-4.2-4.6-4.2-7.6a4.2 4.2 0 0 1 8.4 0C11.2 8.4 7 13 7 13z"/><circle cx="7" cy="5.4" r="1.5"/></svg>
          Dietetics: Level 1, 88 Tolley Street, Richmond VIC 3121
        </li>
        <li class="contact__item">
          <svg class="contact__icon" viewBox="0 0 14 14" aria-hidden="true"><path d="M7 13s-4.2-4.6-4.2-7.6a4.2 4.2 0 0 1 8.4 0C11.2 8.4 7 13 7 13z"/><circle cx="7" cy="5.4" r="1.5"/></svg>
          Training: Private Studio, behind 517 Merrow St, Armadale, VIC, 3143
        </li>
      </ul>
    </div>

    <svg class="card__bands" viewBox="0 0 620 40" aria-hidden="true">
      <polygon points="0,22 486,12 486,40 0,40" fill="var(--plum)"/>
      <polygon points="496,8 620,5 620,40 496,40" fill="var(--deep-blue)"/>
    </svg>
  </section>

  <section class="card card--services" aria-label="Services side">
    <div class="brand">
      <span class="brand__dot" aria-hidden="true"></span>
      <span class="brand__name">Plum Stride</span>
    </div>

    <ul class="services">
      <li class="services__item">Dietetic Consultations, weight loss coaching programs.</li>
      <li class="services__item">Personal and group training, post injury rehab.</li>
      <li class="services__item">Health and nutrition presentations and Health Retreats.</li>
    </ul>
    <p class="web">WWW.PLUMSTRIDE.COM.AU</p>

    <svg class="card__bands" viewBox="0 0 620 40" aria-hidden="true">
      <polygon points="0,22 486,12 486,40 0,40" fill="var(--plum)"/>
      <polygon points="496,8 620,5 620,40 496,40" fill="var(--deep-blue)"/>
    </svg>
  </section>

</main>
</body>
</html>
```